Brisk Mend - Handyman and Home Repair Services

I need a business card/letterhead logo for my new handyman service in my local area. I'm happy for a logo design to be done prior to business card design so it can be incorporated on to the card, for which I'd be happy to pay more for. I'd like it to be modern and not using the typical pictures of tools and cartoon characters in dungarees! I like the idea of tools but in a more modern way i.e subtle background images in different shades to main colour. I do like the american retro designs and those that show age and patina for example, having an image half old, half new in its appearance to represent the repairing of things. Colours in mind are 1950's retro colours, ie using grey with pastel greens, red and cream. I'd like to break the mould and the stigma thats attached to these jobs and make it more cool and up to date. I hope this will attract interior designers and more modern businesses to use my services.

This is the logo design I like and would be happy for this idea and colours:

http://pavo-sunlark.co.uk/wp-content/uploads/2011/01/p-s_logo600px.png

Industry/Entity Type

Handyman

```html
<!DOCTYPE html>
<html lang="en">
<head>
<meta charset="utf-8">
<title>Brisk Mend – Business Card</title>
<link rel="stylesheet" href="https://fonts.googleapis.com/css2?family=Arimo:wght@400;700&display=swap">
<style>
  :root {
    --page: #ece8e2;
    --card-grey: #7a7a7a;
    --card-grey-light: #858585;
    --footer-dark: #545454;
    --footer-text: #c4c4c4;
    --band-blue: #5a93bb;
    --band-blue-soft: #7fb0d2;
    --footer-blue: #2b5b7c;
    --mark-blue: #4a90d4;
    --white: #ffffff;
    --band-text: #e9f0f5;
  }
  * { box-sizing: border-box; margin: 0; padding: 0; }
  html, body {
    width: 1200px; height: 1050px; overflow: hidden;
    background: var(--page);
    font-family: "Arimo", Arial, sans-serif;
  }
  .card {
    position: absolute;
    left: 310px;
    width: 579px;
    height: 330px;
    background: linear-gradient(135deg, var(--card-grey-light), var(--card-grey));
    overflow: hidden;
  }
  .card--front { top: 140px; }
  .card--back { top: 503px; height: 327px; }

  /* front */
  .brand {
    position: absolute;
    left: 0; right: 0; top: 138px;
    display: flex; align-items: center; justify-content: center;
    gap: 10px;
  }
  .brand__square {
    width: 42px; height: 42px;
    background: var(--mark-blue);
  }
  .brand__name {
    color: var(--white);
    font-weight: 700;
    font-size: 44px;
    letter-spacing: -0.5px;
    line-height: 1;
  }
  .card__footer {
    position: absolute;
    left: 0; right: 0; bottom: 0;
    height: 39px;
    display: flex; align-items: center; justify-content: center;
    font-weight: 700;
    font-size: 12px;
  }
  .card--front .card__footer {
    background: var(--footer-dark);
    color: var(--footer-text);
  }

  /* back */
  .holder {
    position: absolute;
    left: 36px; top: 36px;
    color: var(--white);
  }
  .holder__name { font-weight: 700; font-size: 18px; }
  .holder__role {
    font-weight: 700; font-size: 10px;
    margin-left: 72px; margin-top: 2px;
  }
  .service-band {
    position: absolute;
    left: 0; top: 110px;
    width: 100%; height: 106px;
    background: linear-gradient(90deg, var(--band-blue) 0%, var(--band-blue) 66%, var(--band-blue-soft) 82%, rgba(127,176,210,0) 100%);
    display: flex; align-items: center; justify-content: center;
  }
  .service-band__text {
    color: var(--band-text);
    font-weight: 700;
    font-size: 25px;
    line-height: 1.2;
    text-align: center;
    margin-left: -12px;
  }
  .website {
    position: absolute;
    right: 14px; top: 269px;
    color: var(--white);
    font-weight: 700; font-size: 11px;
  }
  .card--back .card__footer {
    height: 36px;
    background: var(--footer-blue);
    color: var(--white);
    font-size: 12px;
  }
</style>
</head>
<body>
  <section class="card card--front">
    <div class="brand">
      <span class="brand__square"></span>
      <span class="brand__name">Brisk Mend</span>
    </div>
    <div class="card__footer">For more info contact us now : 00-000-000</div>
  </section>

  <section class="card card--back">
    <div class="holder">
      <div class="holder__name">Owen Hartley</div>
      <div class="holder__role">Manager</div>
    </div>
    <div class="service-band" role="img" aria-label="Blue band with a speckled texture fading out at the right">
      <p class="service-band__text">Handyman services from<br>repair to instal</p>
    </div>
    <div class="website">website www.briskmend.co.uk</div>
    <div class="card__footer">For more info contact us now : 07700 900461</div>
  </section>
</body>
</html>
```